Business Card Design Project - Amber Ridge

We are looking for a new business card design. Our company name is Amber Ridge Communication Solutions. Our primary function is to provide our clients with communication solutions. These solutions include commercial phone systems and T1 and Fiber Internet lines. Another major part of the business is cabling new buildings with CAT5 cable for both data and phone.

Industry/Entity Type

Communication

Requirements
Must have
• The cards need to be two sided and have some bleeding edge color.
Nice to have
• We are going to upload our current logo BUT we are not married to this logo. If you want to incorporate a re-designed logo with the new business card - please feel free to do so. We are looking for a new bold look that is very colorful yet professional.

```html
<!DOCTYPE html>
<html lang="en">
<head>
<meta charset="utf-8">
<title>Amber Ridge Business Card</title>
<link href="https://fonts.googleapis.com/css2?family=Arimo:wght@400;700&family=Questrial&display=swap" rel="stylesheet">
<style>
  :root {
    --page-bg: #d9d9d9;
    --brand-light: #0b62b0;
    --brand-dark: #0a2c62;
    --navy: #10305e;
    --white: #ffffff;
    --ink: #1c1c1c;
  }
  * { margin: 0; padding: 0; box-sizing: border-box; }
  html, body { width: 1200px; height: 900px; overflow: hidden; }
  body {
    background: var(--page-bg);
    position: relative;
    font-family: "Arimo", Arial, sans-serif;
  }
  .card {
    position: absolute;
    top: 313px;
    width: 478px;
    height: 293px;
  }
  .card-front {
    left: 125px;
    border-radius: 15px 4px 4px 15px;
    background: linear-gradient(110deg, var(--brand-light) 0%, #0a4a93 45%, var(--brand-dark) 100%);
  }
  .card-back {
    left: 610px;
    border-radius: 4px 15px 15px 4px;
    background: var(--white);
  }
  .wordmark {
    position: absolute;
    font-family: "Questrial", "Century Gothic", sans-serif;
    font-weight: 400;
  }
  .wordmark .brand-name { display: block; white-space: nowrap; }
  .wordmark .brand-tagline {
    display: block;
    text-transform: uppercase;
    line-height: 1.15;
  }
  .front-brand {
    left: 60px;
    top: 122px;
    color: var(--white);
  }
  .front-brand .brand-name { font-size: 40px; line-height: 44px; }
  .front-brand .brand-tagline { font-size: 12px; padding-left: 108px; margin-top: 2px; }
  .back-brand {
    left: 187px;
    top: 30px;
    color: var(--navy);
  }
  .back-brand .brand-name { font-size: 24px; line-height: 27px; }
  .back-brand .brand-tagline { font-size: 8px; padding-left: 64px; margin-top: 1px; }
  .name-band {
    position: absolute;
    left: 185px;
    right: 0;
    top: 108px;
    height: 49px;
    background: var(--navy);
    color: var(--white);
    font-weight: 700;
    font-size: 22px;
    letter-spacing: 0.5px;
    line-height: 49px;
    padding-left: 20px;
  }
  .contact {
    position: absolute;
    left: 185px;
    top: 170px;
    font-size: 14px;
    line-height: 19px;
    color: var(--ink);
    list-style: none;
  }
  .contact li { display: flex; align-items: center; gap: 5px; }
  .contact svg { width: 12px; height: 12px; fill: var(--navy); flex: none; }
</style>
</head>
<body>
  <section class="card card-front" aria-label="Card front">
    <div class="wordmark front-brand">
      <span class="brand-name">Amber Ridge</span>
      <span class="brand-tagline">Communication<br>Solutions</span>
    </div>
  </section>

  <section class="card card-back" aria-label="Card back">
    <div class="wordmark back-brand">
      <span class="brand-name">Amber Ridge</span>
      <span class="brand-tagline">Communication<br>Solutions</span>
    </div>
    <div class="name-band">MARCUS WHITFIELD</div>
    <ul class="contact">
      <li>1480 W Sandstone Avenue, Suite 300</li>
      <li>Redmesa, AZ 85099</li>
      <li>
        <svg viewBox="0 0 12 12" aria-label="Phone"><path d="M1 4c0-2 2-3 5-3s5 1 5 3l-2 1-1-2H4L3 5zM2 6h8l1 5H1z"/></svg>
        555.204.3187 or 800.555.0142 (24/7)
      </li>
      <li>
        <svg viewBox="0 0 12 12" aria-label="Fax"><path d="M3 1h5l1 1v3H3zM1 5h10v6H1zM3 7h6v1H3zm0 2h6v1H3z"/></svg>
        800.555.0198
      </li>
      <li>
        <svg viewBox="0 0 12 12" aria-label="Mobile"><path d="M3 0h6v12H3zM4 1.5v7.5h4V1.5zM5.5 10h1v1h-1z"/></svg>
        555.318.6620
      </li>
    </ul>
  </section>
</body>
</html>
```